Hi,

I have just started up a business called VOLMIRA in Melbourne. We run fun street art tours around Melbourne's CBD.

I need to create a design for the back side of my business cards. I have designed the front side (simply with my logo) however, I am having trouble designing the reverse side in a professional manner. I have attached pictures of what I have done.

The picture attached titled "VOLMIRA Business Cards Back" has all the information that I require on the back side of my business cards; although displayed in an amateur and simple way. As displayed in the picture, I need: the VOLMIRA logo, the website URL, the booking details (phone - 0468 152 837 & email - bookings@volmira-example.com.au) and the service description ($20, One Hour, Tours Daily, Meet at Halberton St Station). I would also like to use the font in the picture supplied which is "source-sans-pro".

The VOLMIRA tours are for tourists and are relaxed, entertaining and fun! I would like the design to reflect this.

Target Market(s)

Backpackers & University Students

Industry/Entity Type

Business

Requirements
Must have
• The VOLMIRA logo, the website URL, the booking details (phone - 0468 152 837 & email - bookings@volmira-example.com.au) and the service description ($20, One Hour, Tours Daily, Meet at Halberton St Station).

```html
<!DOCTYPE html>
<html lang="en">
<head>
<meta charset="utf-8">
<title>VOLMIRA – Business Card Back</title>
<link rel="stylesheet" href="https://fonts.googleapis.com/css2?family=Ubuntu:wght@400;500;700&display=swap">
<style>
  :root {
    --page-bg: #e9e9eb;
    --card-white: #ffffff;
    --card-grey: #f1f1f2;
    --ink: #1c1c1c;
    --ink-soft: #4a4f5a;
    --brand-red: #e0241f;
    --brand-red-dark: #b5140f;
    --rule: #d5d5d8;
  }
  * { margin: 0; padding: 0; box-sizing: border-box; }
  html, body {
    width: 1200px; height: 977px; overflow: hidden;
    background: var(--page-bg);
    font-family: "Ubuntu", "Source Sans Pro", sans-serif;
    color: var(--ink);
  }
  .card-back {
    position: absolute; left: 100px; top: 202px;
    width: 1000px; height: 572px;
    background: var(--card-white);
    box-shadow: 0 18px 40px rgba(0,0,0,.18);
    overflow: hidden;
  }
  .brand {
    position: absolute; left: 150px; top: 42px;
    display: flex; align-items: center; gap: 16px;
  }
  .brand__square { width: 30px; height: 30px; background: var(--brand-red); }
  .brand__name {
    font-size: 58px; font-weight: 700; letter-spacing: 3px; color: var(--ink);
  }
  .step {
    position: absolute; font-size: 34px; font-weight: 700; line-height: 1.05; color: var(--ink);
  }
  .step--price { left: 60px; top: 152px; }
  .step--daily { left: 230px; top: 180px; }
  .step--hour { left: 470px; top: 230px; }
  .step--meet { left: 720px; top: 292px; }
  .arrow { position: absolute; width: 56px; height: 18px; }
  .arrow--1 { left: 150px; top: 162px; }
  .arrow--2 { left: 390px; top: 232px; }
  .arrow--3 { left: 640px; top: 300px; }
  .web-ribbon {
    position: absolute; left: 560px; top: 178px; width: 440px; height: 56px;
  }
  .web-ribbon__text {
    position: absolute; left: 600px; top: 190px;
    font-size: 27px; font-weight: 500; color: #fff; letter-spacing: .5px;
  }
  .contact-band {
    position: absolute; left: 0; top: 418px; width: 100%; height: 154px;
    background: linear-gradient(180deg, var(--card-grey), #e6e6e8);
    border-top: 2px solid var(--rule);
  }
  .book-pill {
    position: absolute; left: 200px; top: 396px;
    padding: 10px 22px; border-radius: 8px;
    background: linear-gradient(180deg, #ffffff, #e4e4e6);
    box-shadow: 0 3px 6px rgba(0,0,0,.2);
    font-size: 24px; font-weight: 700; color: var(--ink);
  }
  .book-pill__cta { color: var(--brand-red); }
  .contact {
    position: absolute; top: 478px; display: flex; align-items: center; gap: 16px;
    font-size: 34px; font-weight: 500; color: var(--ink-soft); letter-spacing: 1px;
  }
  .contact--phone { left: 40px; }
  .contact--email { left: 420px; }
  .contact__icon { width: 40px; height: 40px; flex: none; }
</style>
</head>
<body>
<main class="card-back">
  <div class="brand">
    <span class="brand__square"></span>
    <span class="brand__name">VOLMIRA</span>
  </div>

  <div class="step step--price">$20</div>
  <svg class="arrow arrow--1" viewBox="0 0 56 18"><path d="M0 7h40V0l16 9-16 9v-7H0z" fill="var(--brand-red)"/></svg>
  <div class="step step--daily">Tours<br>Daily</div>
  <svg class="arrow arrow--2" viewBox="0 0 56 18"><path d="M0 7h40V0l16 9-16 9v-7H0z" fill="var(--brand-red)"/></svg>
  <div class="step step--hour">One<br>Hour</div>
  <svg class="arrow arrow--3" viewBox="0 0 56 18"><path d="M0 7h40V0l16 9-16 9v-7H0z" fill="var(--brand-red)"/></svg>
  <div class="step step--meet">Meet at<br>Halberton St<br>Station</div>

  <svg class="web-ribbon" viewBox="0 0 440 56" preserveAspectRatio="none">
    <path d="M0 0H440V56H30L0 28Z" fill="var(--brand-red)"/>
    <path d="M0 28L30 56V50Z" fill="var(--brand-red-dark)"/>
  </svg>
  <div class="web-ribbon__text">www.volmira-example.com.au</div>

  <div class="contact-band"></div>
  <div class="book-pill">Call Theo to <span class="book-pill__cta">BOOK NOW</span></div>

  <div class="contact contact--phone">
    <svg class="contact__icon" viewBox="0 0 40 40">
      <circle cx="20" cy="20" r="18" fill="none" stroke="var(--brand-red)" stroke-width="2.5"/>
      <path d="M14 11c2 0 3 4 3 5s-2 2-2 3c1 3 3 5 6 6 1 0 2-2 3-2s5 1 5 3-2 4-4 4c-7 0-14-7-14-14 0-2 2-5 3-5z" fill="var(--brand-red)"/>
    </svg>
    <span>0468 152 837</span>
  </div>
  <div class="contact contact--email">
    <svg class="contact__icon" viewBox="0 0 40 40">
      <circle cx="20" cy="20" r="18" fill="none" stroke="var(--brand-red)" stroke-width="2.5"/>
      <rect x="10" y="13" width="20" height="14" fill="none" stroke="var(--brand-red)" stroke-width="2"/>
      <path d="M10 13l10 8 10-8" fill="none" stroke="var(--brand-red)" stroke-width="2"/>
    </svg>
    <span>bookings@volmira-example.com.au</span>
  </div>
</main>
</body>
</html>
```